Dateierstellung/ Vektor für Folierer Pferdetransporter
Zielgruppe
Reiten-
Aufgabenstellung
Bitte das identische Design übernehmen und auf das Auto anpassen von der Größe, Verteilung auf dem Transporter anpassen und anpassen des Pferdekopfes nach unserem Foto vom Pferd. Das Bild vom Pferd wie auf der Vorlage in schwarz weiß , mit Trense , mit Stirnriemen in der Farbe, mit eingeflochtener Mähne mit der Blesse vom Original Pferd!!!
Rechte Seite : Der Kopf nur auf die Seite wo nicht die Klappe ist, sonst wird das sicher nicht passen?
Hinten Heck wie auf dem Foto Datei erstellen.
Linke Seite Streifen mit Pferdekopf und Text.
Bitte als Datei mit hoher Auflösung das es in der Größe vom Transporter gedruckt werden kann und Vektor für den Folierer.
Bitte alle drei Seiten !

```html
<!DOCTYPE html>
<html lang="de">
<head>
<meta charset="utf-8">
<title>Hufklang – Transporter Beschriftung</title>
<link rel="stylesheet" href="https://fonts.googleapis.com/css2?family=Montserrat:wght@400&display=swap">
<style>
  :root{
    --stage:#808080;
    --panel:#ffffff;
    --teal:#036f66;
    --ink:#111111;
    --horse-dark:#2a2a2a;
    --horse-mid:#6e6e6e;
  }
  *{margin:0;padding:0;box-sizing:border-box}
  html,body{width:1200px;height:1200px;overflow:hidden;background:var(--stage)}
  body{position:relative;font-family:"Montserrat",Arial,sans-serif;color:var(--ink)}
  .side{position:absolute;background:var(--panel);overflow:hidden}
  .side--left-plain{left:37px;top:112px;width:676px;height:450px}
  .side--left-splash{left:37px;top:638px;width:676px;height:450px}
  .side--rear{left:748px;top:327px;width:415px;height:547px}

  .brand{position:absolute;text-align:center;color:var(--teal);font-weight:400;
    text-transform:uppercase;white-space:nowrap;line-height:1}
  .side--left-plain .brand,.side--left-splash .brand{left:0;width:470px;top:168px;font-size:54px;letter-spacing:7px;text-indent:7px}
  .side--rear .brand{left:0;width:415px;top:148px;font-size:50px;letter-spacing:6px;text-indent:6px}

  .divider{position:absolute}
  .side--left-plain .divider,.side--left-splash .divider{left:112px;top:298px;width:246px;height:34px}
  .side--rear .divider{left:58px;top:279px;width:299px;height:42px}

  .tagline{position:absolute;left:40px;width:390px;top:352px;font-size:13.4px;letter-spacing:.6px;
    text-align:center;white-space:nowrap;text-transform:uppercase}
  .tagline__sep{color:var(--teal);font-size:9px;margin:0 6px;vertical-align:1px}

  .motto{position:absolute;left:0;width:415px;top:337px;font-size:19px;line-height:26px;
    letter-spacing:3px;text-align:center;text-transform:uppercase}

  .horse-photo{position:absolute;left:438px;top:99px;width:238px;height:351px;
    background:radial-gradient(ellipse at 55% 40%,var(--horse-mid) 0%,var(--horse-dark) 60%,rgba(42,42,42,.85) 100%);
    border-radius:46% 0 0 0 / 30% 0 0 0}
  .splash{position:absolute;left:0;top:0;width:676px;height:450px}

  .heart-emblem{position:absolute;left:137px;top:409px;width:140px;height:107px;
    background:var(--teal);border-radius:50% 50% 50% 50% / 45% 45% 55% 55%}
</style>
</head>
<body>

<section class="side side--left-plain" aria-label="Linke Seite Streifen">
  <div class="brand">Hufklang</div>
  <svg class="divider" viewBox="0 0 246 34" aria-hidden="true">
    <path d="M0 17 L96 16 L96 18 Z M150 16 L246 17 L150 18 Z" fill="var(--teal)"/>
    <rect x="113" y="7" width="20" height="20" transform="rotate(45 123 17)" fill="none" stroke="var(--teal)" stroke-width="2.4"/>
    <rect x="118" y="12" width="10" height="10" transform="rotate(45 123 17)" fill="var(--teal)"/>
  </svg>
  <p class="tagline">Leidenschaft<span class="tagline__sep">◆</span>Vertrauen<span class="tagline__sep">◆</span>Partnerschaft</p>
  <div class="horse-photo" role="img" aria-label="Schwarz-weiß Foto eines Pferdekopfes mit Blesse"></div>
</section>

<section class="side side--left-splash" aria-label="Linke Seite Streifen mit Farbwelle">
  <div class="brand">Hufklang</div>
  <svg class="divider" viewBox="0 0 246 34" aria-hidden="true">
    <path d="M0 17 L96 16 L96 18 Z M150 16 L246 17 L150 18 Z" fill="var(--teal)"/>
    <rect x="113" y="7" width="20" height="20" transform="rotate(45 123 17)" fill="none" stroke="var(--teal)" stroke-width="2.4"/>
    <rect x="118" y="12" width="10" height="10" transform="rotate(45 123 17)" fill="var(--teal)"/>
  </svg>
  <p class="tagline">Leidenschaft<span class="tagline__sep">◆</span>Vertrauen<span class="tagline__sep">◆</span>Partnerschaft</p>
  <div class="horse-photo" role="img" aria-label="Schwarz-weiß Foto eines Pferdekopfes mit Blesse"></div>
  <svg class="splash" viewBox="0 0 676 450" role="img" aria-label="Türkis-schwarze Farbwelle mit Glitzerpartikeln">
    <defs>
      <linearGradient id="splashTone" x1="0" y1="1" x2="1" y2="0">
        <stop offset="0" stop-color="#ffffff" stop-opacity="0"/>
        <stop offset=".35" stop-color="#1a1a1a" stop-opacity=".7"/>
        <stop offset=".7" stop-color="#1fb3a6"/>
        <stop offset="1" stop-color="#2fd6c8"/>
      </linearGradient>
    </defs>
    <path d="M135 420 C260 380 420 420 520 360 C590 320 640 270 676 230 L676 450 L220 450 Z" fill="url(#splashTone)"/>
  </svg>
</section>

<section class="side side--rear" aria-label="Heck">
  <div class="brand">Hufklang</div>
  <svg class="divider" viewBox="0 0 299 42" aria-hidden="true">
    <path d="M0 21 L118 20 L118 22 Z M182 20 L299 21 L182 22 Z" fill="var(--teal)"/>
    <rect x="137" y="8" width="26" height="26" transform="rotate(45 150 21)" fill="none" stroke="var(--teal)" stroke-width="3"/>
    <rect x="143" y="14" width="14" height="14" transform="rotate(45 150 21)" fill="var(--teal)"/>
  </svg>
  <p class="motto">Zwei Herzen<br>im gleichen Takt.</p>
  <div class="heart-emblem" role="img" aria-label="Illustration zweier Pferdeköpfe, die ein Herz bilden"></div>
</section>

</body>
</html>
```